Simple graphic for a book or slide presentation

We are looking for a style that suits the style of our book. It's title is Harbor. Keeping a calm course through stormy seas. There will be more line drawing/graphics in the book but how you design this image will create the style for all the other simple graphics in the book (once we decide what they are). So this one design will lead to a few more to match the style of this one. We'd like the shape of the overall graphic (i.e the arrows and words/bubbles) to be circular (not a rounded square as appears in the sample attached). Perhaps the words don't need to be in ovals or bound by anything at all; perhaps they do - let's see what you see. We'd like you to choose a font or offer many different fonts you think will capture the practical yet unconventional tone of the book. The book is teaching that managing risks in life is a life-skill that can be learned. The section of the book where this graphic will be placed is called "the power of language" - basically we are saying that thoughts, words and actions create our culture and our destiny. This insight comes from Torvel Pelloru's famous quote:
Carefully watch your thoughts, for they become your words.
Manage and watch your words, for they will become your actions.
Consider and judge your actions, for they have become your habits.
Acknowledge and watch your habits, for they shall become your values.
Understand and embrace your values, for they become your destiny.

Please change the text in the middle of the graphic to say: The Human Culture Cycle

```html
<!DOCTYPE html>
<html lang="en">
<head>
<meta charset="utf-8">
<title>The Human Culture Cycle</title>
<link rel="stylesheet" href="https://fonts.googleapis.com/css2?family=Roboto:wght@500;700&display=swap">
<style>
  :root {
    --page: #ffffff;
    --frame: #5a5a5a;
    --ring-dark: #2b2b2b;
    --ring-light: #727272;
    --hub-dark: #262626;
    --hub-light: #595959;
    --label: #ffffff;
  }
  html, body {
    margin: 0;
    padding: 0;
    width: 1200px;
    height: 1200px;
    overflow: hidden;
    background: var(--page);
  }
  .canvas {
    display: block;
    width: 1200px;
    height: 1200px;
  }
  .page-frame {
    fill: none;
    stroke: var(--frame);
    stroke-width: 1.5;
  }
  .ring-stop-dark { stop-color: var(--ring-dark); }
  .ring-stop-light { stop-color: var(--ring-light); }
  .hub-stop-dark { stop-color: var(--hub-dark); }
  .hub-stop-light { stop-color: var(--hub-light); }
  .cycle-step { fill: url(#ringShade); }
  .hub { fill: url(#hubShade); }
  .step-label {
    font-family: "Roboto", Arial, sans-serif;
    font-weight: 500;
    font-size: 31px;
    letter-spacing: 1.5px;
    fill: var(--label);
    text-anchor: middle;
  }
  .hub-title {
    font-family: "Roboto", Arial, sans-serif;
    font-weight: 700;
    font-size: 45px;
    letter-spacing: 2.5px;
    fill: var(--label);
    text-anchor: middle;
  }
</style>
</head>
<body>
<svg class="canvas" viewBox="0 0 1200 1200" xmlns="http://www.w3.org/2000/svg">
  <defs>
    <radialGradient id="ringShade" gradientUnits="userSpaceOnUse" cx="600" cy="600" r="304">
      <stop offset="0.77" class="ring-stop-dark"/>
      <stop offset="0.885" class="ring-stop-light"/>
      <stop offset="1" class="ring-stop-dark"/>
    </radialGradient>
    <radialGradient id="hubShade" gradientUnits="userSpaceOnUse" cx="600" cy="600" r="152">
      <stop offset="0" class="hub-stop-light"/>
      <stop offset="1" class="hub-stop-dark"/>
    </radialGradient>
    <path id="stepShape" d="M610.6,296.2 A304,304 0 0 1 852,430 L833.8,465 L795.6,468 A236,236 0 0 0 608.2,364.1 L628.2,331.5 Z"/>
    <path id="clockwiseTrack" d="M471,823.4 A258,258 0 1 1 729,376.6 A258,258 0 1 1 471,823.4"/>
    <path id="lowerTrack" d="M318,600 A282,282 0 0 0 882,600"/>
  </defs>

  <rect class="page-frame" x="1" y="1" width="1198" height="1198"/>

  <g class="cycle-ring">
    <use class="cycle-step" href="#stepShape" transform="rotate(-60 600 600)"/>
    <use class="cycle-step" href="#stepShape"/>
    <use class="cycle-step" href="#stepShape" transform="rotate(60 600 600)"/>
    <use class="cycle-step" href="#stepShape" transform="rotate(120 600 600)"/>
    <use class="cycle-step" href="#stepShape" transform="rotate(180 600 600)"/>
    <use class="cycle-step" href="#stepShape" transform="rotate(240 600 600)"/>
  </g>

  <g class="cycle-labels">
    <text class="step-label"><textPath href="#clockwiseTrack" startOffset="16.2%">VALUES</textPath></text>
    <text class="step-label"><textPath href="#clockwiseTrack" startOffset="33.0%">CULTURE</textPath></text>
    <text class="step-label"><textPath href="#clockwiseTrack" startOffset="49.8%">THOUGHTS</textPath></text>
    <text class="step-label"><textPath href="#clockwiseTrack" startOffset="66.2%">WORDS</textPath></text>
    <text class="step-label"><textPath href="#lowerTrack" startOffset="67.5%">ACTIONS</textPath></text>
    <text class="step-label"><textPath href="#lowerTrack" startOffset="34.5%">HABITS</textPath></text>
  </g>

  <circle class="hub" cx="600" cy="600" r="152"/>
  <text class="hub-title">
    <tspan x="600" y="543">THE</tspan>
    <tspan x="600" y="592">HUMAN</tspan>
    <tspan x="600" y="641">CULTURE</tspan>
    <tspan x="600" y="690">CYCLE</tspan>
  </text>
</svg>
</body>
</html>
```